Construction Website Design for your platform

Update:
I like this theme as a starting point. It seems like a very good start. Fonts, colors, motion, etc. https://consultancy.qrvistaweb.com/
***************************************************************************************

I want a new website design that can be implemented in your platform. Here is my existing site: www.halvornquantax.com
Attached is a document with the copy, requirements, sample images, etc. Let me know what questions you have.

Here is a sample of the info, but review the attached document for everything:

Website layout:
Title Bar
• Home
• Expertise
• Takeoffs
• Divisions Serviced (redesign from orig page: (http://www.halvornquantax.com/scope-list/)
• Member Login
Requirements
• Home page has a slider with 3 dimmed commercial construction images and copy overlay
• Request for Proposal Form should be over the slider and the same look and location on every page.
• “Request For Proposal” – No Obligation
o Company Name
o Contact Name
o Contact Phone
o Contact Email
• Use the copy below for the pages
• Split the Client Testimonials among the pages

Target Market(s)

B2B - Construction Companies

Industry/Entity Type

Construction

Number of Pages Required

4 page

Font styles to use
Serif

Colors
0255a3
3276b5
85abd2
d0dfed

Requirements
Must have
• Construction images in slider
• Request for proposal form
• testimonials

```html
<!DOCTYPE html>
<html lang="en">
<head>
<meta charset="utf-8">
<title>Halvorn Quantax</title>
<link href="https://fonts.googleapis.com/css2?family=Montserrat:wght@300;400;500;600;700;800&family=Raleway:wght@300;400;700;800&family=Open+Sans:wght@400;600&display=swap" rel="stylesheet">
<style>
:root{
  --navy:#233f8c;
  --navy-dark:#1b3274;
  --blue:#0255a3;
  --blue-mid:#3276b5;
  --sky:#2aa6e0;
  --pale:#e3f4f8;
  --topbar:#e4f5f8;
  --ink:#333;
  --grey:#777;
  --footer:#3a3a3a;
  --footer-base:#2b2b2b;
  --white:#fff;
}
*{box-sizing:border-box;margin:0;padding:0}
html,body{width:1200px;height:2476px;overflow:hidden}
body{position:relative;font-family:"Open Sans",Arial,sans-serif;color:var(--ink);background:var(--white)}
.abs{position:absolute}

/* top bar */
.topbar{left:0;top:0;width:1200px;height:25px;background:var(--topbar);font:400 12px "Montserrat",sans-serif;color:var(--navy)}
.topbar .links{right:48px;top:5px;display:flex;gap:24px}
.topbar svg{vertical-align:-2px;margin-right:5px}

/* header */
.header{left:0;top:25px;width:1200px;height:87px;background:var(--white)}
.brand{left:60px;top:26px;color:var(--navy);font:600 30px/1 "Montserrat",sans-serif;letter-spacing:.5px;display:flex;align-items:center;gap:10px;white-space:nowrap}
.brand i{display:inline-block;width:12px;height:12px;background:currentColor}
.contact{font:400 14px "Montserrat",sans-serif;color:var(--ink)}
.contact.phone{left:745px;top:20px}
.contact.hours{left:955px;top:20px}
.contact svg{position:absolute;left:0;top:8px}
.contact div{padding-left:46px;line-height:26px;white-space:nowrap}
.contact a{color:var(--navy);text-decoration:none}

/* nav */
.nav{left:0;top:112px;width:1200px;height:75px;background:linear-gradient(180deg,var(--navy),var(--navy-dark));font:400 14px "Montserrat",sans-serif;color:var(--white)}
.nav ul{list-style:none;display:flex;position:absolute;left:65px;top:30px}
.nav li{padding:0 20px;border-left:1px solid rgba(255,255,255,.3);line-height:14px}
.nav li:first-child{border:0;padding-left:0;color:var(--sky)}
.nav .caret{margin-left:8px;font-size:10px}
.nav .search{right:68px;top:30px}

/* hero */
.hero{left:0;top:187px;width:1200px;height:598px;overflow:hidden;
  background:radial-gradient(ellipse at 30% 70%,#b88a3e 0%,#6e5630 25%,transparent 55%),
             linear-gradient(180deg,#3c4f80 0%,#2a3350 40%,#3a3022 75%,#22242c 100%)}
.hero-title{left:46px;top:222px;font:700 70px "Montserrat",sans-serif;color:var(--white);letter-spacing:1px}
.hero-sub{left:46px;top:318px;font:400 14px "Montserrat",sans-serif;color:var(--white)}
.hero-title span{color:var(--sky)}
.btn-ghost{left:48px;top:387px;width:136px;height:37px;border:2px solid var(--white);color:var(--white);font:500 12px "Montserrat",sans-serif;display:flex;align-items:center;justify-content:center;gap:10px}

.rfp-ring{left:690px;top:75px;width:508px;height:508px;border-radius:50%;background:rgba(30,90,170,.3)}
.rfp{left:706px;top:91px;width:476px;height:476px;border-radius:50%;background:rgba(33,130,205,.88)}
.rfp-title{left:770px;top:140px;width:320px;text-align:center;color:var(--white);font:500 18px "Montserrat",sans-serif;letter-spacing:.5px}
.rfp-frame{left:788px;top:138px;width:290px;height:42px}
.rfp-rule{left:890px;top:195px;width:80px;height:2px;background:var(--white)}
.rfp-text{left:790px;top:210px;width:280px;text-align:center;color:var(--white);font:400 12px/1.8 "Montserrat",sans-serif}
.field{width:190px;height:43px;background:var(--white);font:500 11px "Montserrat",sans-serif;color:var(--ink);padding:15px 10px;letter-spacing:.3px}
.submit{left:853px;top:400px;width:157px;height:50px;background:var(--navy-dark);border:1px solid rgba(255,255,255,.5);color:var(--white);font:600 12px "Montserrat",sans-serif;display:flex;align-items:center;justify-content:center}

/* intro */
.intro-title{left:0;top:870px;width:1200px;text-align:center;font:700 36px "Montserrat",sans-serif;color:var(--navy)}
.intro-title span{font-weight:300}
.intro-tag{left:0;top:930px;width:1200px;text-align:center;font:400 16px "Montserrat",sans-serif;color:var(--ink)}
.intro-copy{left:100px;top:984px;width:1000px;text-align:center;font:400 12.5px/26px "Open Sans",sans-serif;color:var(--grey)}

.feature-icon{width:80px;height:80px;border-radius:50%;background:var(--navy)}
.feature h3{font:400 21px "Montserrat",sans-serif;color:var(--navy);margin-bottom:6px;padding-left:3px}
.feature p{font:400 12.5px/23px "Open Sans",sans-serif;color:var(--grey);text-align:justify}

/* band */
.band{left:0;top:1371px;width:1200px;height:220px;background:var(--pale)}
.band h2{position:absolute;left:66px;top:62px;font:300 36px "Raleway",sans-serif;color:#555}
.band h2 b{font-weight:800;color:var(--navy)}
.band p{position:absolute;left:66px;top:108px;width:800px;font:300 18px/26px "Raleway",sans-serif;color:#999;letter-spacing:.4px}
.btn-frame{position:absolute;left:886px;top:93px;width:163px;height:49px;border:2px solid var(--navy);color:var(--navy);font:600 14px "Montserrat",sans-serif;display:flex;align-items:center;justify-content:center;gap:12px}
.btn-frame::before,.btn-frame::after{content:"";position:absolute;width:10px;height:10px}
.btn-frame::before{right:-8px;top:-8px;border-top:2px solid var(--navy);border-right:2px solid var(--navy)}
.btn-frame::after{left:-8px;bottom:-8px;border-bottom:2px solid var(--navy);border-left:2px solid var(--navy)}

/* testimonials */
.reviews{left:0;top:1657px;width:1200px;height:538px;border-top:4px solid #1c3c6a;
  background:linear-gradient(180deg,#1d4c7c 0%,#215c8e 45%,#1b5388 100%)}
.reviews h2{position:absolute;left:0;top:44px;width:1200px;text-align:center;font:700 36px "Montserrat",sans-serif;color:var(--white)}
.reviews h2 span{font-weight:300}
.reviews .sub{position:absolute;left:0;top:106px;width:1200px;text-align:center;font:500 15px "Montserrat",sans-serif;color:var(--white)}
.quote{position:absolute;width:450px}
.quote svg.mark{position:absolute;left:0;top:4px}
.quote p{margin-left:63px;font:400 13.5px/27px "Montserrat",sans-serif;color:var(--white);text-align:justify}
.avatar{position:absolute;width:70px;height:70px;border-radius:50%;background:linear-gradient(135deg,#c9a38a,#6a4a3a);border:3px solid var(--white)}
.person{position:absolute;font:700 13px "Montserrat",sans-serif;color:var(--white)}
.person em{display:block;font:italic 400 12px "Montserrat",sans-serif;margin-top:8px}

/* footer */
.footer{left:0;top:2201px;width:1200px;height:225px;background:var(--footer);color:#ddd;font:400 12px "Montserrat",sans-serif}
.footer .brand{left:88px;top:44px;color:var(--white);font-size:24px}
.footer .brand i{width:10px;height:10px}
.f-addr{top:118px;line-height:22px}
.f-phone{top:174px}
.footer h4{position:absolute;font:500 14px "Montserrat",sans-serif;color:var(--white);letter-spacing:.3px}
.footer ul{position:absolute;list-style:none;line-height:27px;font-size:11.5px}
.footer li::before{content:"·";margin-right:16px}
.social{left:957px;top:85px;width:168px;height:46px;background:var(--white);color:var(--navy);font:600 22px "Montserrat",sans-serif;display:flex;align-items:center;justify-content:center}
.cards{left:957px;top:190px;display:flex;gap:6px}
.cards span{width:39px;height:24px;background:var(--white);border-radius:2px}
.copyright{left:0;top:2426px;width:1200px;height:50px;background:var(--footer-base);color:#bbb;font:400 11px/50px "Montserrat",sans-serif;text-align:center}
</style>
</head>
<body>

<div class="abs topbar">
  <div class="abs links">
    <span><svg width="11" height="11" viewBox="0 0 11 11"><path d="M4 1H1v9h3M4 5.5h6M7 3l3 2.5L7 8" fill="none" stroke="currentColor" stroke-width="1.4"/></svg>Signup</span>
    <span><svg width="8" height="11" viewBox="0 0 8 11"><rect x="1" y=".5" width="6" height="10" rx="1" fill="none" stroke="currentColor"/></svg>Contact</span>
  </div>
</div>

<header class="abs header">
  <div class="abs brand"><i></i>HALVORN QUANTAX</div>
  <div class="abs contact phone">
    <svg width="30" height="34" viewBox="0 0 30 34"><rect x="6" y="2" width="14" height="28" rx="2" fill="none" stroke="var(--navy)" stroke-width="2.4"/><path d="M23 12a5 5 0 0 1 0 8M26 9a9 9 0 0 1 0 14" fill="none" stroke="var(--navy)" stroke-width="1.8"/></svg>
    <div>(555) 014-3870<br><a>desk@hqtakeoffs.com</a></div>
  </div>
  <div class="abs contact hours">
    <svg width="32" height="32" viewBox="0 0 32 32"><circle cx="16" cy="16" r="13" fill="none" stroke="var(--navy)" stroke-width="2.6"/><path d="M16 8v8l6 4" fill="none" stroke="var(--navy)" stroke-width="2.6"/></svg>
    <div>9 am to 8 pm<br>Monday - Saturday</div>
  </div>
</header>

<nav class="abs nav">
  <ul>
    <li>Home</li>
    <li>Expertise<span class="caret">&#8964;</span></li>
    <li>Takeoffs<span class="caret">&#8964;</span></li>
    <li>Divisions Serviced<span class="caret">&#8964;</span></li>
    <li>Members Login</li>
  </ul>
  <svg class="abs search" width="14" height="14" viewBox="0 0 14 14"><circle cx="6" cy="6" r="4.5" fill="none" stroke="#fff" stroke-width="2"/><path d="M9.5 9.5L13 13" stroke="#fff" stroke-width="2"/></svg>
</nav>

<section class="abs hero" role="img" aria-label="Dimmed night photo of a commercial construction site with tower cranes and lit building frames">
  <div class="abs hero-title">C<span>O</span>NFIDENCE</div>
  <div class="abs hero-sub">Accurate and reliable, we help you propose on more work without risk.</div>
  <div class="abs btn-ghost">Read More <span>&#8250;</span></div>

  <div class="abs rfp-ring"></div>
  <div class="abs rfp"></div>
  <svg class="abs rfp-frame" viewBox="0 0 290 42" fill="none" stroke="#fff" stroke-width="1.5"><path d="M0 12V0h12M278 0h12v12M290 30v12h-12M12 42H0V30"/></svg>
  <div class="abs rfp-title">REQUEST FOR PROPOSAL</div>
  <div class="abs rfp-rule"></div>
  <div class="abs rfp-text">Lorem Ipsum is simply dummy text of the printing and typesetting industry.</div>
  <div class="abs field" style="left:734px;top:275px">COMPANY NAME</div>
  <div class="abs field" style="left:932px;top:275px">CONTACT NAME</div>
  <div class="abs field" style="left:734px;top:331px">PHONE</div>
  <div class="abs field" style="left:932px;top:331px">EMAIL ADDRESS</div>
  <div class="abs submit">SUBMIT</div>
</section>

<h1 class="abs intro-title">HALVORN <span>QUANTAX</span></h1>
<div class="abs intro-tag">We cover a rage of industries as diverse as you expected...</div>
<p class="abs intro-copy">Dedicated to saving our clients time and money by specializing in accurate, reliable materials quantity calculations, Halvorn Quantax allows general contractors to confidently propose on more work with less stress. To receive a no-obligation answer to your takeoff needs complete the Request for Proposal form. Halvorn Quantax will provide a comprehensive proposal detailing the hours required and payment options that are easily refined to both near- and long-term needs.</p>

<div class="abs feature-icon" style="left:51px;top:1115px">
  <svg width="80" height="80" viewBox="0 0 80 80" fill="none" stroke="#fff" stroke-width="3"><circle cx="40" cy="40" r="17"/><circle cx="40" cy="23" r="5" fill="var(--navy)"/><circle cx="25" cy="49" r="5" fill="var(--navy)"/><circle cx="55" cy="49" r="5" fill="var(--navy)"/></svg>
</div>
<div class="abs feature" style="left:155px;top:1110px;width:406px">
  <h3>Process</h3>
  <p>Once the proposal is approved, clients fund their account and allocate their hours as desired - project-by-project, monthly, as-needed, or otherwise. Our service and products are completely tailored to each client based on the fundamental factors that make your business distinct from all others.</p>
</div>

<div class="abs feature-icon" style="left:620px;top:1115px">
  <svg width="80" height="80" viewBox="0 0 80 80" fill="none" stroke="#fff" stroke-width="3"><path d="M26 26v28h28"/><path d="M31 47l8-9 6 5 9-11M49 32h5v5"/></svg>
</div>
<div class="abs feature" style="left:723px;top:1110px;width:402px">
  <h3>Benefits</h3>
  <p>Accurate, reliable quantities delivered as-scheduled and expected allow your key staff to invest their time in quality, safety, profit, and client relationships. An extra set of hands in your bid room helps you put out more proposals and takes a tedious task off your to-do list whenever you need it without the obligation of a full-time salary.</p>
</div>

<section class="abs band">
  <h2>The <b>Cutting Edge of Business</b></h2>
  <p>Unlike other Frameworks which try to cover everything, it has been built specifically for your platform. Aliquam sapien est, mollis id mattis id, scelerisque sed dolor.</p>
  <div class="btn-frame">Read More <span>&#8594;</span></div>
</section>

<section class="abs reviews" role="img" aria-label="Blurred blue-toned photo of a construction site with cranes behind client testimonials">
  <h2>CLIENTS <span>REMARK</span></h2>
  <div class="sub">The best of the best is here...</div>

  <div class="quote" style="left:110px;top:212px">
    <svg class="mark" width="40" height="36" viewBox="0 0 40 36" fill="#fff"><path d="M2 0h14v16L8 34H2l5-16H2zM22 0h14v16l-8 18h-6l5-16h-5z"/></svg>
    <p>Halvorn Quantax does outstanding work, accurate, detailed, and reliable. The consultant on my account knows what I want in the breakdown and produces the information exactly as I need it.Time, money and confidence, Halvorn Quantax hits the mark every time.”</p>
  </div>
  <div class="avatar" style="left:109px;top:374px" role="img" aria-label="Client portrait"></div>
  <div class="person" style="left:195px;top:388px">Dana Whitcomb, President<em>- Northfield Roofing</em></div>

  <div class="quote" style="left:645px;top:212px">
    <svg class="mark" width="40" height="36" viewBox="0 0 40 36" fill="#fff"><path d="M2 0h14v16L8 34H2l5-16H2zM22 0h14v16l-8 18h-6l5-16h-5z"/></svg>
    <p>We get an influx of great opportunities and sometimes it's more than we can handle. Halvorn Quantax fills the gap and helped us to grow our business. It's really excellent to have a genuine, always-ready ally in our estimating efforts.</p>
  </div>
  <div class="avatar" style="left:652px;top:374px" role="img" aria-label="Client portrait"></div>
  <div class="person" style="left:738px;top:388px">Ravi Ostrand<em>- Harborline Builders, LLC.</em></div>
</section>

<footer class="abs footer">
  <div class="abs brand"><i></i>HALVORN QUANTAX</div>
  <svg class="abs" style="left:102px;top:118px" width="14" height="20" viewBox="0 0 14 20"><path d="M7 0a7 7 0 0 0-7 7c0 5 7 13 7 13s7-8 7-13a7 7 0 0 0-7-7z" fill="#fff"/><circle cx="7" cy="7" r="2.6" fill="var(--footer)"/></svg>
  <div class="abs f-addr" style="left:136px">Halvorn Quantax, Po Box-418,<br>Brenton Falls, GA30000</div>
  <svg class="abs" style="left:102px;top:176px" width="16" height="16" viewBox="0 0 16 16"><path d="M3 1l3 3-2 2c1 2 3 4 6 6l2-2 3 3-2 2C7 15 1 9 1 3z" fill="#fff"/></svg>
  <div class="abs f-phone" style="left:136px">(555) 014-3870</div>

  <h4 style="left:484px;top:50px">QUICK LINKS</h4>
  <ul style="left:484px;top:90px"><li>Expertise</li><li>Takeoffs</li><li>Divisions Serviced</li></ul>

  <h4 style="left:698px;top:50px">CUSTOMER INFO</h4>
  <ul style="left:706px;top:90px"><li>Customer Signup</li><li>Privacy Policy</li><li>Contact</li></ul>

  <h4 style="left:957px;top:50px">FOLLOW US @</h4>
  <div class="abs social">Bidhall</div>
  <h4 style="left:957px;top:160px">WE PROUDLY ACCEPT:</h4>
  <div class="abs cards" role="img" aria-label="Accepted payment methods"><span></span><span></span><span></span><span></span></div>
</footer>

<div class="abs copyright">Copyright © 2019 Halvorn Quantax, All rights reserved.</div>

</body>
</html>
```